Roll Up Banner for Lifestyle / medical company

I need a roll-up banner for a congress highlighting our lifestyle company that aids people with diabetes type 2 through diet and exercise. The banner should capture our unique approach and appeal to medical professionals.

120x200 cm

Scope of work
- Design a roll-up banner for a congress.
- Include the programme name: Ons Suikerpad Route Schema.
- Add the catchphrase: Het individuele leefstijlprogramma voor 50-plussers met diabetes type 2.
- Feature the 4 pillars: Digitaal en persoonlijk, Duurzame begeleiding, Bewezen resultaten, Aanvulling ketenzorg.

References
- See our style at voedwijzerkracht.nl and in the files attached

Additional information
The banner should appeal to medical professionals attending the congress.

Company details
- Company website: voedwijzerkracht.nl
- We are a lifestyle company dedicated to helping people manage diabetes type 2 through tailored diet and exercise programs. Our target audience for this banner is medical professionals.

We can provide photo's of older individuals in our style. Contact us at info@voedwijzerkracht.nl for these pictures.

```html
<!DOCTYPE html>
<html lang="nl">
<head>
<meta charset="utf-8">
<title>Ons Suikerpad Route Schema – roll-up banner</title>
<link rel="stylesheet" href="https://fonts.googleapis.com/css2?family=Outfit:wght@500;600;700&family=Oswald:wght@600&display=swap">
<style>
  :root {
    --page-bg: #e6e7e6;
    --mint: #dcece0;
    --mint-light: #e9f4ec;
    --forest: #1e5645;
    --ink: #2e5043;
    --teal: #2aa99a;
    --teal-line: #5fb5ac;
    --cream: #eef5e6;
    --white: #ffffff;
  }
  * { box-sizing: border-box; margin: 0; padding: 0; }
  html, body { width: 1040px; height: 1200px; overflow: hidden; }
  body {
    background: var(--page-bg);
    font-family: "Outfit", "Helvetica Neue", Arial, sans-serif;
    position: relative;
  }
  .banner {
    position: absolute;
    left: 190px; top: 18px;
    width: 660px; height: 1164px;
    background: var(--mint);
    overflow: hidden;
  }
  .hero { position: absolute; inset: 0 0 auto 0; height: 788px; }
  .connectors { position: absolute; inset: 0; }
  .title {
    position: absolute; left: 55px; top: 64px;
    font-weight: 700; font-size: 62px; line-height: 78px;
    letter-spacing: -1.5px; color: var(--ink);
    white-space: nowrap;
  }
  .title .accent { color: var(--teal); }
  .brand {
    position: absolute; left: 470px; top: 82px;
    width: 128px; height: 132px;
    background: var(--forest); border-radius: 20px;
    display: flex; align-items: center; padding-left: 16px;
    color: var(--white); font-weight: 600; font-size: 20px; line-height: 23px;
  }
  .photo { position: absolute; border-radius: 4px; }
  .photo-man {
    left: 352px; top: 224px; width: 216px; height: 222px;
    background: linear-gradient(180deg, #d9e6dc 0%, #c9b3a4 45%, #8a6a58 100%);
  }
  .photo-woman {
    left: 62px; top: 416px; width: 250px; height: 372px;
    background: linear-gradient(180deg, #d8e4da 0%, #e0cdb4 35%, #c99a8e 100%);
  }
  .tagline {
    position: absolute; left: 315px; top: 446px;
    width: 345px; height: 163px;
    background: var(--mint-light);
    border: 2px solid var(--teal-line); border-right: none;
    border-radius: 14px 0 0 14px;
    padding: 12px 0 0 24px;
    font-weight: 500; font-size: 24px; line-height: 34px; color: var(--ink);
    white-space: nowrap;
  }
  .pillars-band {
    position: absolute; left: 0; bottom: 0;
    width: 100%; height: 376px; background: var(--forest);
  }
  .pillars {
    position: absolute; left: 60px; top: 44px;
    display: grid; grid-template-columns: 297px 260px; row-gap: 27px;
    list-style: none;
  }
  .pillar { display: flex; align-items: center; gap: 33px; }
  .pillar svg { width: 56px; height: 56px; flex: none; }
  .pillar-text {
    color: var(--white); font-weight: 500; font-size: 28px; line-height: 36px;
    white-space: nowrap;
  }
  .url {
    position: absolute; left: 59px; top: 264px;
    width: 541px; height: 65px; border-radius: 33px;
    background: var(--cream);
    display: flex; align-items: center; justify-content: center;
    font-family: "Oswald", "Arial Narrow", sans-serif; font-weight: 600;
    font-size: 38px; letter-spacing: 0.5px; color: var(--forest);
    white-space: nowrap;
  }
</style>
</head>
<body>
  <main class="banner">
    <section class="hero">
      <svg class="connectors" width="660" height="788" viewBox="0 0 660 788" fill="none" stroke="var(--teal-line)" stroke-width="2.5">
        <path d="M598 148 H605 Q617 148 617 160 V434 Q617 446 605 446 H568"/>
        <path d="M316 600 V620 Q316 632 328 632 H466 Q478 632 478 644 V709 Q478 721 466 721 H371 Q359 721 359 709 V673 Q359 661 347 661 H312"/>
        <path d="M62 712 H45 Q33 712 33 724 V788"/>
      </svg>

      <h1 class="title">ons<br>suikerpad<br><span class="accent">route</span><br><span class="accent">schema</span></h1>

      <div class="brand">voedwijzer<br>kracht</div>

      <div class="photo photo-man" role="img" aria-label="Foto: oudere man met koffiekop kijkt naar zijn telefoon"></div>
      <div class="photo photo-woman" role="img" aria-label="Foto: oudere vrouw in roze blazer kijkt naar haar telefoon"></div>

      <p class="tagline">Het individuele<br>leefstijlprogramma<br>voor 50-plussers<br>met diabetes type 2</p>
    </section>

    <section class="pillars-band">
      <ul class="pillars">
        <li class="pillar">
          <svg viewBox="0 0 56 56" fill="none" stroke="var(--teal)" stroke-width="3" stroke-linecap="round">
            <circle cx="8" cy="14" r="4"/><circle cx="8" cy="42" r="4"/><circle cx="48" cy="10" r="4"/><circle cx="48" cy="46" r="4"/>
            <path d="M12 14 H20 V24 H28"/><path d="M12 42 H20 V32 H28"/>
            <path d="M44 10 H36 V24"/><path d="M44 46 H36 V32"/>
            <path d="M28 6 V50"/>
          </svg>
          <span class="pillar-text">Digitaal en<br>persoonlijk</span>
        </li>
        <li class="pillar">
          <svg viewBox="0 0 56 56" fill="none" stroke="var(--teal)" stroke-width="3" stroke-linecap="round" stroke-linejoin="round">
            <rect x="10" y="8" width="36" height="44" rx="4"/><rect x="20" y="4" width="16" height="8" rx="2"/>
            <path d="M18 24 H20 M26 24 H38 M18 33 H20 M26 33 H38 M18 42 H20 M26 42 H38"/>
          </svg>
          <span class="pillar-text">Bewezen<br>resultaten</span>
        </li>
        <li class="pillar">
          <svg viewBox="0 0 56 56" fill="none" stroke="var(--teal)" stroke-width="3" stroke-linecap="round" stroke-linejoin="round">
            <path d="M8 48 Q6 14 48 8 Q50 46 14 44 Z"/><path d="M8 48 L34 22"/>
          </svg>
          <span class="pillar-text">Duurzame<br>begeleiding</span>
        </li>
        <li class="pillar">
          <svg viewBox="0 0 56 56" fill="none" stroke="var(--teal)" stroke-width="3.5" stroke-linecap="round">
            <path d="M24 20 L32 12 a8 8 0 0 1 12 12 L36 32"/><path d="M32 36 L24 44 a8 8 0 0 1 -12 -12 L20 24"/>
            <path d="M22 34 L34 22"/>
          </svg>
          <span class="pillar-text">Aanvulling<br>ketenzorg</span>
        </li>
      </ul>
      <div class="url">WWW.VOEDWIJZERKRACHT.NL</div>
    </section>
  </main>
</body>
</html>
```